Re-design of current business cards

We are updating our website with new colors and layout. Would like to re-design our business cards to co-ordinate. See attached pdf with new Brindlecraft website colors. We would also like to combine our 2 brands on the one business card. Attached is the new design for our Brindlecraft website, current business cards, which are one sided, brindlecraft logo in tiff, .ai for fonts. Brindlecraft logo font is Optimum, Quillmarsh website home page image, Quillmarsh brand statics for products which includes the logo for this brand.

Quillmarsh brand will stay the dark gray on the website. See attached statics for product and website home page.
Updates

The business cards will be 2 sided. Brindlecraft Brand on one side and Quillmarsh Brand on the other. The colors for Brindlecraft need to follow the color scheme of the brindlecraft website pdf I uploaded. The colors are a blue, lighter teal blue and white. Quillmarsh needs to follow the dark gray color on files uploaded

Target Market(s)

The trade and consumers

Industry/Entity Type

Home Furnishing

Contact Information for Business Card

We are updating our website with new colors and layout. Would like to re-design our business cards to co-ordinate. We would also like to combine our 2 brands onto 1 2 sided business cards.

Requirements
Must have
• Colors that match our new website, see attached image.
• RGB colors
• navy -#152842
• teal - 98aeb9
• The gray color used for Quillmarsh brands.
• ll logos and fonts should stay the same.

```html
<!DOCTYPE html>
<html lang="en">
<head>
<meta charset="utf-8">
<title>Brindlecraft and Quillmarsh business card</title>
<link href="https://fonts.googleapis.com/css2?family=Roboto:wght@400;700&family=Roboto+Condensed:wght@300;400;700&display=swap" rel="stylesheet">
<style>
  :root {
    --navy: #152842;
    --teal: #98aeb9;
    --paper: #f7f7f6;
    --rule: #cfd0d2;
    --ink-gray: #6d6f72;
    --charcoal: #1c1e21;
    --charcoal-text: #e9e9e9;
    --band: #e4e4e4;
    --band-text: #3a3b3d;
    --backdrop: #e8e6e2;
  }
  * { margin: 0; padding: 0; box-sizing: border-box; }
  html, body { width: 1200px; height: 911px; overflow: hidden; background: var(--backdrop); }
  .sheet {
    width: 1200px; height: 911px;
    display: flex; flex-direction: column; align-items: center; justify-content: center; gap: 52px;
  }
  .card {
    width: 660px; height: 377px; position: relative; overflow: hidden;
    box-shadow: 0 6px 18px rgba(0,0,0,0.18);
  }

  /* Brindlecraft side */
  .card--brand { background: var(--paper); }
  .edge-stripe { position: absolute; left: 0; top: 0; bottom: 0; width: 12px; background: var(--teal); }
  .edge-stripe::before { content: ""; position: absolute; left: 0; top: 0; width: 100%; height: 82px; background: var(--navy); }
  .brand-mark {
    position: absolute; left: 12px; top: 0; width: 268px; height: 100%;
    display: flex; flex-direction: column; align-items: center; justify-content: center; gap: 18px;
  }
  .brand-mark__dot { width: 46px; height: 46px; border-radius: 50%; background: var(--navy); }
  .brand-mark__name {
    font-family: "Roboto Condensed", sans-serif; font-weight: 300; font-size: 36px; letter-spacing: 2px;
    color: var(--ink-gray); text-transform: uppercase;
  }
  .column-rule { position: absolute; left: 292px; top: 46px; bottom: 46px; width: 1px; background: var(--rule); }
  .contact { position: absolute; left: 322px; top: 58px; font-family: "Roboto", sans-serif; color: var(--ink-gray); }
  .contact__name { font-family: "Roboto Condensed", sans-serif; font-weight: 700; font-size: 26px; color: var(--navy); text-transform: uppercase; letter-spacing: 0.3px; }
  .contact__role { font-family: "Roboto Condensed", sans-serif; font-size: 17px; text-transform: uppercase; line-height: 1.25; margin-top: 4px; }
  .contact__address { font-size: 15px; line-height: 1.4; margin-top: 14px; }
  .contact__lines { list-style: none; margin-top: 14px; font-size: 15px; line-height: 1.55; }
  .contact__lines li { display: flex; align-items: center; gap: 9px; }
  .contact__lines svg { width: 13px; height: 13px; fill: var(--navy); flex: none; }

  /* Quillmarsh side */
  .card--collection { background: var(--charcoal); }
  .collection-title {
    position: absolute; left: 0; right: 0; top: 66px; text-align: center;
    font-family: "Roboto Condensed", sans-serif; font-weight: 300; font-size: 64px; letter-spacing: 6px;
    color: var(--charcoal-text); text-transform: uppercase; line-height: 1;
  }
  .collection-tagline {
    position: absolute; left: 0; right: 0; top: 168px; text-align: center;
    font-family: "Roboto Condensed", sans-serif; font-weight: 400; font-size: 25px; color: var(--charcoal-text);
  }
  .collection-band {
    position: absolute; left: 0; right: 0; top: 262px; height: 68px; background: var(--band);
    display: flex; flex-direction: column; justify-content: center; align-items: center;
    font-family: "Roboto Condensed", sans-serif; font-size: 16px; line-height: 1.35; color: var(--band-text);
  }
</style>
</head>
<body>
<main class="sheet">
  <section class="card card--brand" aria-label="Brindlecraft side">
    <div class="edge-stripe"></div>
    <div class="brand-mark">
      <div class="brand-mark__dot"></div>
      <div class="brand-mark__name">Brindlecraft</div>
    </div>
    <div class="column-rule"></div>
    <div class="contact">
      <h1 class="contact__name">Dana Whitlow</h1>
      <p class="contact__role">Graphics<br>Photography Director</p>
      <p class="contact__address">PO Box 412/1870 Larkspur Ridge Rd<br>Fairhaven, Virginia 24099</p>
      <ul class="contact__lines">
        <li><svg viewBox="0 0 16 16" aria-hidden="true"><path d="M3.5 1l3 3-1.7 2.2c.9 2 2.5 3.6 4.5 4.5L11.5 9l3 3-2 2.5C6.5 14 2 9.5 1 3.5z"/></svg>555.014.2210</li>
        <li><svg viewBox="0 0 16 16" aria-hidden="true"><path d="M4 1h6l2 2v3H4zM1 7h14v6h-2v2H3v-2H1zm4 4v3h6v-3z"/></svg>555.014.2287</li>
        <li><svg viewBox="0 0 16 16" aria-hidden="true"><path d="M1 3h14v10H1zm1.5 1.5L8 9l5.5-4.5z"/></svg>dwhitlow@brindlecraft.com</li>
        <li><svg viewBox="0 0 16 16" aria-hidden="true"><circle cx="8" cy="8" r="6.2" fill="none" stroke="currentColor" stroke-width="1.6" style="stroke: var(--navy)"/><path d="M1.8 7.3h12.4v1.4H1.8zM7.3 1.8h1.4v12.4H7.3z"/></svg>www.brindlecraft.com</li>
      </ul>
    </div>
  </section>

  <section class="card card--collection" aria-label="Quillmarsh side">
    <h2 class="collection-title">Quillmarsh</h2>
    <p class="collection-tagline">Discover the luxury of home.</p>
    <div class="collection-band">
      <p>Exclusive Designs | Limited Distribution | Generous Proportion</p>
      <p>Limited Introduction October 2015 Full Collection Launch April 2016</p>
    </div>
  </section>
</main>
</body>
</html>
```